Aviation Consultant Seeking a Business Wordpress Site

I am looking for a Wordpress website for my small (it's just me) airport noise consulting firm. We work with airports to address aircraft noise issues in nearby communities. We also work with communities to help them understand aircraft noise and flight operations, air traffic control, etc., and to come up with strategies for collaborating with the airport to address noise and overflight issues.

I'd like a contemporary design that is both professional and modern.

My firm's services include establishing noise abatement programs for airports, working with airports, aviation industry (airlines, air traffic controllers, airports), and the community (neighborhoods located near noisy airports), to reduce noise impacts associated with aircraft operations.

My clients are primarily airports, but I also work with communities located near airports.

We provide technical support to help communities understand the complexities of aircraft noise and aviation. We also work to help airports understand the interests and concerns of their community.

Our tagline is: "Listen · Partner · Resolve"

and "bridging the gap between airports and their communities"

A couple examples of site designs I love are:

http://slidecraftstudio.example.co.uk/
http://www.quirkmoth.example.com/
http://risenbloomkids.example.com/

I found this template which I like a lot: http://glidepanelsampler.example.com/ I'm wondering if they have similar templates for Wordpress.

I am very open to your recommendations on design. I've worked on two projects on ArtHive and have been extremely pleased with the outcomes.

Thank you for your interest in my project!

Target Market(s)

Airports, communities located near airports, city governments, national airspace bureau

Industry/Entity Type

Airport

Font styles to use
Sans Serif

Requirements
Must have
• Professional look and feel.
Nice to have
• I envision a one page website (with multiple sections that you can scroll up/down to like the template I listed above. I am open to multiple pages if you think that would look/work better. Sections would include:
• Welcome (top section or home page)
• Who We Are
• What We Do
• Why HNP?
• Contact Us
• Within the What We Do section, there will be graphics representing specialty areas such as:
• Noise Office Management
• Noise Program Development/Expansion
• Hush Route Programs
• Stakeholder Engagement
• SkyPath / RNX
• These are just ideas. I am open to your expert recommendations and creativity.
• Here are some wordpress templates I like:
• http://demo.layoutforge.example.com/?theme=soloist&device=desktop&_ga=1.482917365.9083716254.2961748305
• http://skinwright.example/demo/themes/depthshift/#
• http://skinbazaar.example.net/item/q-the-skin/full_screen_preview/3926418
• http://lumora.skins.example
Should not have
• Should not be a blog or designed like a blog. I do not plan on a blogging component. This should be designed as a modern, small business website.

```html
<!DOCTYPE html>
<html lang="en">
<head>
<meta charset="utf-8">
<title>Harbor Noise Partners</title>
<link rel="stylesheet" href="https://fonts.googleapis.com/css2?family=Cinzel:wght@400;700&family=Arimo:wght@400;700&display=swap">
<style>
  :root {
    --brand-blue: #4468a8;
    --nav-grey: #5b5b5b;
    --band-grey: #e8e8e8;
    --ink: #1c1c1c;
    --body-text: #2b2b2b;
    --white: #ffffff;
    --field-bg: #f4f4f4;
    --field-text: #8a8a8a;
    --submit-bg: #2e2e2e;
    --footer-bg: #565656;
    --rule-grey: #d8d8d8;
    --icon-pale: #e2e8f3;
    --tagline-grey: #555555;
  }
  * { box-sizing: border-box; margin: 0; padding: 0; }
  html, body { width: 1200px; height: 2532px; overflow: hidden; background: var(--white); }
  body { position: relative; font-family: "Arimo", Arial, sans-serif; color: var(--body-text); }

  .site-header { position: absolute; left: 0; top: 0; width: 1200px; height: 194px; background: var(--white); }
  .brand { position: absolute; left: 118px; top: 30px; display: flex; align-items: center; }
  .brand-dot { width: 70px; height: 70px; border-radius: 50%; background: var(--brand-blue); flex: none; }
  .brand-text { margin-left: 16px; }
  .brand-name { font-family: "Cinzel", serif; font-weight: 400; font-size: 25px; color: var(--brand-blue); letter-spacing: 0.5px; line-height: 30px; }
  .brand-tagline { font-family: "Arimo", Arial, sans-serif; font-size: 15px; color: var(--tagline-grey); letter-spacing: 2px; line-height: 22px; margin-top: 3px; }

  .main-nav { position: absolute; left: 167px; top: 138px; width: 868px; height: 54px; background: var(--nav-grey); border-radius: 4px 4px 0 0; }
  .main-nav a { position: absolute; top: 0; line-height: 54px; font-size: 19px; color: var(--white); text-decoration: none; transform: translateX(-50%); }
  .nav-divider { position: absolute; top: 12px; width: 1px; height: 30px; background: #8a8a8a; }

  .hero-photo { position: absolute; left: 0; top: 194px; width: 1200px; height: 386px;
    background: linear-gradient(160deg, #1d3a86 0%, #3f5fa8 45%, #8fa3c8 75%, #d9dbe2 100%); }

  .welcome-band { position: absolute; left: 0; top: 580px; width: 1200px; height: 358px; background: var(--band-grey); }
  .welcome-card { position: absolute; left: 135px; top: 543px; width: 922px; height: 358px; background: var(--brand-blue); border-radius: 5px; color: var(--white); text-align: center; }
  .welcome-title { font-family: "Cinzel", serif; font-weight: 700; font-size: 27px; letter-spacing: 0.5px; margin-top: 40px; line-height: 36px; }
  .welcome-copy { font-size: 14px; line-height: 22.5px; margin: 20px auto 0; width: 860px; }
  .welcome-copy + .welcome-copy { margin-top: 22px; }
  .btn-outline { position: absolute; left: 351px; top: 266px; width: 189px; height: 50px; border: 2px solid var(--white); font-family: "Cinzel", serif; font-size: 19px; line-height: 46px; color: var(--white); text-decoration: none; }

  .section-title { position: absolute; left: 0; width: 1200px; text-align: center; font-family: "Cinzel", serif; font-weight: 700; font-size: 42px; color: var(--ink); line-height: 56px; letter-spacing: 0.5px; }
  .section-rule { position: absolute; left: 375px; width: 432px; height: 3px; background: var(--rule-grey); }

  .about { position: absolute; left: 110px; top: 1064px; width: 960px; text-align: center; }
  .about-copy { font-size: 17.5px; line-height: 26.5px; color: var(--body-text); }
  .about-copy + .about-copy { margin-top: 26px; }

  .service-card { position: absolute; top: 1445px; width: 228px; height: 272px; text-align: center; }
  .service-card.is-active { background: var(--brand-blue); }
  .service-icon { position: absolute; left: 53px; top: 23px; width: 122px; height: 122px; border-radius: 50%; background: var(--icon-pale); }
  .service-card.is-active .service-icon { background: var(--white); }
  .service-text { position: absolute; left: 14px; top: 178px; width: 200px; font-size: 14.5px; line-height: 22.5px; color: #222; }
  .service-card.is-active .service-text { color: var(--white); }

  .contact-section { position: absolute; left: 0; top: 1864px; width: 1200px; height: 621px;
    background: linear-gradient(135deg, #1e4d92 0%, #2d62ab 45%, #245499 70%, #3a6fb6 100%); }
  .contact-title { position: absolute; left: 0; top: 50px; width: 1200px; text-align: center; font-family: "Cinzel", serif; font-weight: 700; font-size: 42px; color: var(--white); line-height: 56px; letter-spacing: 0.5px; }
  .contact-rule { position: absolute; left: 280px; top: 114px; width: 583px; height: 3px; border-top: 1px solid #a9c0e3; border-bottom: 1px solid #a9c0e3; }
  .field { position: absolute; background: var(--field-bg); border-radius: 3px; font-size: 14px; color: var(--field-text); padding: 17px 11px 0; }
  .field-message { padding-top: 16px; }
  .btn-submit { position: absolute; left: 760px; top: 538px; width: 135px; height: 44px; background: var(--submit-bg); border-radius: 3px; color: var(--white); font-family: "Cinzel", serif; font-weight: 700; font-size: 19px; letter-spacing: 1px; text-align: center; line-height: 44px; }

  .site-footer { position: absolute; left: 0; top: 2485px; width: 1200px; height: 47px; background: var(--footer-bg); color: var(--white); text-align: center; font-size: 13.5px; line-height: 47px; }
</style>
</head>
<body>
  <header class="site-header">
    <div class="brand">
      <div class="brand-dot"></div>
      <div class="brand-text">
        <div class="brand-name">HARBOR NOISE PARTNERS</div>
        <div class="brand-tagline">Listen · Partner · Resolve</div>
      </div>
    </div>
    <nav class="main-nav">
      <a href="#" style="left:100px">HOME</a>
      <span class="nav-divider" style="left:172px"></span>
      <a href="#" style="left:252px">MISSION</a>
      <span class="nav-divider" style="left:333px"></span>
      <a href="#" style="left:417px">SERVICES</a>
      <span class="nav-divider" style="left:503px"></span>
      <a href="#" style="left:572px">WORK</a>
      <span class="nav-divider" style="left:653px"></span>
      <a href="#" style="left:729px">CONTACT</a>
    </nav>
  </header>

  <div class="hero-photo" role="img" aria-label="Photo of a white passenger jet climbing against a blue sky"></div>

  <section class="welcome-band"></section>
  <div class="welcome-card">
    <h1 class="welcome-title">WELCOME TO HARBOR NOISE PARTNERS</h1>
    <p class="welcome-copy">Lorem Ipsum is simply dummy text of the printing and typesetting industry. Lorem Ipsum has been the industry's standard dummy text ever since the 1500s, when an unknown printer took a galley of type and scrambled it to make a type specimen book. It has survived not only five centuries, but also the leap into electronic typesetting, remaining essentially unchanged.</p>
    <p class="welcome-copy">It was popularised in the 1960s with the release of Letterform sheets containing Lorem Ipsum passages, and more recently with desktop publishing software like Quill LayoutDesk including versions of Lorem Ipsum.</p>
    <a class="btn-outline" href="#">READ MORE</a>
  </div>

  <h2 class="section-title" style="top:980px">WHO WE ARE</h2>
  <div class="section-rule" style="top:1043px"></div>
  <div class="about">
    <p class="about-copy">Lorem Ipsum is simply dummy text of the printing and typesetting industry. Lorem Ipsum has been the industry's standard dummy text ever since the 1500s, when an unknown printer took a galley of type and scrambled it to make a type specimen book. It has survived not only five centuries, but also the leap into electronic galley of type and scrambled it to make a type specimen book. It has survived not only typesetting, remaining essentially unchanged.</p>
    <p class="about-copy">It was popularised in the 1960s with the release of Letterform sheets containing Lorem Ipsum passages, and more recently with desktop publishing software like Quill LayoutDesk including versions of Lorem Ipsum.</p>
  </div>

  <h2 class="section-title" style="top:1332px">WHO WE DO</h2>
  <div class="section-rule" style="top:1396px"></div>

  <div class="service-card" style="left:92px">
    <div class="service-icon"></div>
    <p class="service-text">Lorem Ipsum has been the industry's standard dummy text ever 1500s</p>
  </div>
  <div class="service-card is-active" style="left:356px">
    <div class="service-icon"></div>
    <p class="service-text">Lorem Ipsum has been the industry's standard dummy text ever 1500s</p>
  </div>
  <div class="service-card" style="left:620px">
    <div class="service-icon"></div>
    <p class="service-text">Lorem Ipsum has been the industry's standard dummy text ever 1500s</p>
  </div>
  <div class="service-card" style="left:884px">
    <div class="service-icon"></div>
    <p class="service-text">Lorem Ipsum has been the industry's standard dummy text ever 1500s</p>
  </div>

  <section class="contact-section">
    <h2 class="contact-title">CONTACT US</h2>
    <div class="contact-rule"></div>
    <div class="field" style="left:245px;top:153px;width:304px;height:52px">First Name*</div>
    <div class="field" style="left:598px;top:153px;width:297px;height:52px">Last Name*</div>
    <div class="field" style="left:245px;top:239px;width:305px;height:53px">Phone*</div>
    <div class="field" style="left:598px;top:239px;width:297px;height:53px">Email*</div>
    <div class="field" style="left:243px;top:320px;width:652px;height:52px">Airport/Organization*</div>
    <div class="field field-message" style="left:243px;top:398px;width:652px;height:111px">Message*</div>
    <div class="btn-submit">SUBMIT</div>
  </section>

  <footer class="site-footer">© 2015 Harbor Noise Partners Ltd. Powered by Pixel Forge.</footer>
</body>
</html>
```